Design business card using existing logo.

PLEASE DO NOT USE "RED WHITE & BLACK" color combo! Thank you.

Try different color combos such as:
- Vintage colors like brown, orange, gold, blue (not all together but a combo of 1 or 3
- Blue, w/ grey, or silver or white, Blue monochromatic can work as well.
- Use monochromatic variations on back (just an idea)

- Include full name, "Quillmarsh Records" on at least one side.

Target Market(s)

Teens

Industry/Entity Type

Business

Colors
3277b5
ffc214
f04a50
f78f20

```html
<!DOCTYPE html>
<html lang="en">
<head>
<meta charset="utf-8">
<title>Quillmarsh Records – Business Card</title>
<link rel="stylesheet" href="https://fonts.googleapis.com/css2?family=Montserrat:wght@400;600;700&family=Open+Sans:wght@400;600&display=swap">
<style>
  :root {
    --canvas-bg: #e9e7e4;
    --card-dark: #22598a;
    --card-deep: #1b4a75;
    --card-light: #ffffff;
    --accent: #f78f20;
    --accent-gold: #ffc214;
    --ink: #22598a;
    --ink-soft: #3277b5;
    --shadow: rgba(0, 0, 0, 0.18);
  }
  * { box-sizing: border-box; margin: 0; padding: 0; }
  html, body {
    width: 1200px;
    height: 900px;
    overflow: hidden;
    background: var(--canvas-bg);
  }
  .canvas {
    width: 1200px;
    height: 900px;
    display: flex;
    align-items: center;
    justify-content: center;
    gap: 40px;
  }
  .card {
    position: relative;
    width: 540px;
    height: 309px;
    overflow: hidden;
    box-shadow: 0 10px 30px var(--shadow);
  }

  /* Back side */
  .card-back {
    background: linear-gradient(135deg, var(--card-dark), var(--card-deep));
    display: flex;
    flex-direction: column;
    align-items: center;
    justify-content: center;
    gap: 22px;
  }
  .brand-dot {
    width: 96px;
    height: 96px;
    border-radius: 50%;
    background: var(--accent);
  }
  .brand-name {
    font-family: "Montserrat", sans-serif;
    font-weight: 600;
    font-size: 30px;
    letter-spacing: 1px;
    color: var(--card-light);
    white-space: nowrap;
  }

  /* Front side */
  .card-front { background: var(--card-light); }
  .front-wave {
    position: absolute;
    inset: 0;
    width: 100%;
    height: 100%;
  }
  .front-brand {
    position: absolute;
    top: 30px;
    right: 30px;
    display: flex;
    flex-direction: column;
    align-items: center;
    gap: 8px;
  }
  .front-brand .brand-dot {
    width: 78px;
    height: 78px;
  }
  .front-brand .brand-name {
    font-size: 11px;
    color: var(--ink);
    letter-spacing: 1.2px;
  }
  .holder {
    position: absolute;
    left: 40px;
    top: 58px;
  }
  .holder-name {
    font-family: "Montserrat", sans-serif;
    font-weight: 700;
    font-size: 20px;
    text-transform: uppercase;
    line-height: 1.1;
  }
  .holder-name .first { color: var(--accent); }
  .holder-name .last { color: var(--ink); }
  .holder-role {
    font-family: "Open Sans", sans-serif;
    font-weight: 600;
    font-size: 12px;
    color: var(--ink-soft);
    margin-top: 2px;
  }
  .contact {
    position: absolute;
    left: 40px;
    top: 130px;
    font-family: "Open Sans", sans-serif;
    font-size: 14px;
    color: var(--ink);
    list-style: none;
  }
  .contact-item {
    display: flex;
    align-items: center;
    gap: 8px;
    height: 23px;
  }
  .contact-icon {
    width: 17px;
    height: 17px;
    flex: none;
  }
  .contact-address {
    margin-top: 8px;
    line-height: 1.35;
  }
</style>
</head>
<body>
<main class="canvas">

  <section class="card card-back" aria-label="Card back">
    <div class="brand-dot"></div>
    <div class="brand-name">QUILLMARSH RECORDS</div>
  </section>

  <section class="card card-front" aria-label="Card front">
    <svg class="front-wave" viewBox="0 0 540 309" preserveAspectRatio="none" aria-hidden="true">
      <path d="M0,286 C150,314 330,262 540,150 L540,309 L0,309 Z" fill="var(--card-dark)"/>
      <path d="M0,266 C140,300 300,252 482,170 C320,264 150,300 0,280 Z" fill="var(--accent)"/>
    </svg>

    <div class="front-brand">
      <div class="brand-dot"></div>
      <div class="brand-name">QUILLMARSH RECORDS</div>
    </div>

    <header class="holder">
      <h1 class="holder-name"><span class="first">Daniel</span> <span class="last">Hartley</span></h1>
      <p class="holder-role">Managing Director</p>
    </header>

    <ul class="contact">
      <li class="contact-item">
        <svg class="contact-icon" viewBox="0 0 20 20" aria-hidden="true">
          <circle cx="10" cy="10" r="10" fill="var(--accent)"/>
          <path d="M7 5.5l1.6 2.2-.9 1.1c.6 1.2 1.4 2 2.6 2.6l1.1-.9 2.2 1.6-.8 1.6c-3.2-.2-6.3-3.3-6.5-6.5z" fill="#fff"/>
        </svg>
        (044)123456789
      </li>
      <li class="contact-item">
        <svg class="contact-icon" viewBox="0 0 20 20" aria-hidden="true">
          <circle cx="10" cy="10" r="10" fill="var(--accent)"/>
          <rect x="5.5" y="6.5" width="9" height="7" fill="#fff"/>
          <path d="M5.5 6.5l4.5 4 4.5-4" fill="none" stroke="var(--accent)" stroke-width="1"/>
        </svg>
        info@youremail.com
      </li>
      <li class="contact-item">
        <svg class="contact-icon" viewBox="0 0 20 20" aria-hidden="true">
          <circle cx="10" cy="10" r="10" fill="var(--accent)"/>
          <circle cx="10" cy="10" r="4.5" fill="none" stroke="#fff" stroke-width="1.3"/>
          <path d="M5.5 10h9M10 5.5c-1.8 2.4-1.8 6.6 0 9M10 5.5c1.8 2.4 1.8 6.6 0 9" fill="none" stroke="#fff" stroke-width="1"/>
        </svg>
        www.websitename.com
      </li>
      <li class="contact-address">1234, Address GoesHere,<br>Country name, 12345</li>
    </ul>
  </section>

</main>
</body>
</html>
```